Yoga Studio - Class Timetable Flyer

We require a double sided, size DL (1/3 A4) flyer with our class timetable included.
We would like the final flyer to have.
Side A : Yoga image, logo, address, website, contact phone number, and in big font $40 Introductory Month.
Side B: Clear easy to read timetable, class descriptions and website.
Thank you.
Yours kindly,
Hilda
Colors
87d0c7
86cae7
85acd3

```html
<!DOCTYPE html>
<html lang="en">
<head>
<meta charset="utf-8">
<title>Stillwater Flow – Introductory Month Flyer</title>
<link href="https://fonts.googleapis.com/css2?family=Bree+Serif&family=Cabin+Condensed:wght@400;500&display=swap" rel="stylesheet">
<style>
  :root {
    --teal: #66b5c8;
    --teal-light: #86cae7;
    --sea: #87d0c7;
    --mist: #85acd3;
    --white: #ffffff;
    --ink: #1e1e1e;
    --grid-line: #c8b89f;
    --frame: #c9bca6;
    --hot: #e8463a;
    --vinyasa: #a07b55;
    --essentials: #1b75bb;
    --funky: #6b2c8f;
    --yin: #8cc63f;
    --charity: #9b1c5e;
    --crop: #9a9a9a;
  }
  * { box-sizing: border-box; margin: 0; padding: 0; }
  html, body { width: 1200px; height: 904px; overflow: hidden; background: var(--white); }
  body { position: relative; font-family: "Cabin Condensed", sans-serif; color: var(--ink); }

  .crop-marks { position: absolute; inset: 0; }

  /* Side A */
  .side-a { position: absolute; left: 229px; top: 64px; width: 758px; height: 367px; }
  .offer-band {
    position: absolute; left: 0; top: 0; width: 758px; height: 99px;
    background: var(--teal);
    display: flex; align-items: center; justify-content: center; gap: 12px;
    font-family: "Bree Serif", serif; color: var(--white);
    text-shadow: 2px 3px 5px rgba(0,0,0,.35);
  }
  .offer-price { font-size: 64px; line-height: 1; }
  .offer-title { font-size: 44px; line-height: 1; letter-spacing: .5px; }
  .hero-photo {
    position: absolute; left: 3px; top: 99px; width: 753px; height: 267px;
    background: linear-gradient(180deg, #d9eef4 0%, #a9d9e3 35%, var(--sea) 60%, #7fc1cf 100%);
  }
  .hero-shade {
    position: absolute; right: 2px; top: 99px; width: 230px; height: 267px;
    background: linear-gradient(90deg, rgba(102,181,200,0) 0%, var(--teal) 45%);
  }
  .brand { position: absolute; left: 560px; top: 108px; width: 150px; text-align: center; color: var(--white); }
  .brand-dot { width: 44px; height: 44px; border-radius: 50%; background: var(--white); margin: 0 auto 10px; }
  .brand-name { font-family: "Bree Serif", serif; font-size: 27px; line-height: 1; }
  .brand-tagline { font-family: "Cabin Condensed", sans-serif; font-size: 7px; letter-spacing: 1px; margin-top: 4px; }
  .contact {
    position: absolute; right: 28px; top: 250px; text-align: right;
    font-family: "Bree Serif", serif; color: var(--white); font-size: 13.5px; line-height: 17px;
  }
  .contact-phone { font-size: 21px; line-height: 26px; margin-top: 2px; }

  /* Side B */
  .side-b {
    position: absolute; left: 254px; top: 507px; width: 713px; height: 327px;
    border: 1.5px solid var(--frame); border-radius: 10px;
  }
  .timetable {
    position: absolute; left: 4px; top: 5px; width: 445px; height: 318px;
    display: grid; grid-template-columns: 54px repeat(7, 1fr); grid-template-rows: 14px repeat(6, 1fr);
    gap: 2px; background: var(--grid-line); padding: 0 2px 2px;
    border-radius: 6px; overflow: hidden;
  }
  .day { font-family: "Bree Serif", serif; font-size: 7px; text-align: center; line-height: 14px; background: var(--grid-line); color: var(--ink); }
  .time { background: var(--white); font-family: "Bree Serif", serif; font-size: 11px; display: flex; align-items: center; justify-content: center; }
  .slot { background: var(--white); padding: 1px; position: relative; }
  .class {
    height: 100%; display: flex; flex-direction: column; align-items: center; justify-content: center;
    color: var(--white); font-family: "Bree Serif", serif; font-size: 9.5px; line-height: 10px; text-align: center;
  }
  .class small { font-family: "Cabin Condensed", sans-serif; font-size: 7.5px; margin-top: 2px; }
  .class.compact { font-size: 7px; line-height: 8px; }
  .hot { background: var(--hot); }
  .vinyasa { background: var(--vinyasa); }
  .essentials { background: var(--essentials); }
  .funky { background: var(--funky); }
  .yin { background: var(--yin); }
  .charity { display: flex; align-items: center; justify-content: center; height: 100%; }

  .legend {
    position: absolute; left: 453px; top: 5px; width: 255px; height: 316px;
    background: var(--teal); border-radius: 8px; padding: 10px 8px 0 9px;
  }
  .legend-item { display: flex; gap: 9px; align-items: flex-start; }
  .legend-tag {
    flex: none; width: 38px; height: 20px; margin-top: 6px; border: 1.5px solid var(--white); border-radius: 2px;
    color: var(--white); font-family: "Bree Serif", serif; font-size: 6.5px; line-height: 7px;
    display: flex; align-items: center; justify-content: center; text-align: center;
  }
  .legend-star { flex: none; width: 38px; display: flex; justify-content: center; margin-top: 4px; }
  .legend-text { font-size: 10.5px; line-height: 11.5px; color: var(--ink); }
  .legend-item + .legend-item { margin-top: 6px; }
  .legend-web {
    position: absolute; left: 0; right: 0; bottom: 6px; text-align: center;
    font-family: "Bree Serif", serif; color: var(--white); font-size: 15px;
  }
</style>
</head>
<body>

<svg class="crop-marks" width="1200" height="904" aria-hidden="true">
  <g stroke="var(--crop)" stroke-width="0.8">
    <line x1="241" y1="20" x2="241" y2="55"/><line x1="977" y1="20" x2="977" y2="55"/>
    <line x1="241" y1="440" x2="241" y2="475"/><line x1="977" y1="440" x2="977" y2="475"/>
    <line x1="241" y1="862" x2="241" y2="897"/><line x1="977" y1="862" x2="977" y2="897"/>
    <line x1="186" y1="73" x2="222" y2="73"/><line x1="995" y1="73" x2="1031" y2="73"/>
    <line x1="186" y1="421" x2="222" y2="421"/><line x1="995" y1="421" x2="1031" y2="421"/>
    <line x1="186" y1="494" x2="222" y2="494"/><line x1="995" y1="494" x2="1031" y2="494"/>
    <line x1="186" y1="843" x2="222" y2="843"/><line x1="995" y1="843" x2="1031" y2="843"/>
  </g>
</svg>

<section class="side-a">
  <header class="offer-band">
    <span class="offer-price">$40</span>
    <span class="offer-title">INTRODUCTORY MONTH</span>
  </header>
  <div class="hero-photo" role="img" aria-label="Photograph of a woman in white seated in a meditation pose with raised hands at the end of a wooden jetty over calm sea"></div>
  <div class="hero-shade"></div>
  <div class="brand">
    <div class="brand-dot"></div>
    <div class="brand-name">stillwater flow</div>
    <div class="brand-tagline">YOGA • FITNESS • AQUA</div>
  </div>
  <address class="contact">
    42 Wattlebird Lane<br>
    Fernvale • Vic 3999<br>
    www.stillwaterflow.com.au<br>
    hildamoreland@studiomail.com.au
    <div class="contact-phone">0400 555 018</div>
  </address>
</section>

<section class="side-b">
  <div class="timetable">
    <div class="day"></div>
    <div class="day">MONDAY</div><div class="day">TUESDAY</div><div class="day">WEDNESDAY</div>
    <div class="day">THURSDAY</div><div class="day">FRIDAY</div><div class="day">SATURDAY</div><div class="day">SUNDAY</div>

    <div class="time">9:30am</div>
    <div class="slot"></div>
    <div class="slot"><div class="class hot">HOT<small>90 MINUTES</small></div></div>
    <div class="slot"></div>
    <div class="slot"><div class="class vinyasa">POWER<br>VINYASA<small>75 MINUTES</small></div></div>
    <div class="slot"></div>
    <div class="slot"><div class="class vinyasa">POWER<br>VINYASA<small>90 MINUTES</small></div></div>
    <div class="slot"></div>

    <div class="time">11:00am</div>
    <div class="slot"></div><div class="slot"></div><div class="slot"></div>
    <div class="slot"><div class="class essentials compact">POWER<br>ESSENTIALS<small>60 MINUTES</small></div></div>
    <div class="slot"></div><div class="slot"></div><div class="slot"></div>

    <div class="time">1:00pm</div>
    <div class="slot"></div><div class="slot"></div>
    <div class="slot"><div class="class hot">HOT<small>90 MINUTES</small></div></div>
    <div class="slot"></div><div class="slot"></div><div class="slot"></div><div class="slot"></div>

    <div class="time">4:30pm</div>
    <div class="slot"></div><div class="slot"></div><div class="slot"></div><div class="slot"></div><div class="slot"></div><div class="slot"></div>
    <div class="slot"><div class="class vinyasa">POWER<br>VINYASA<small>90 MINUTES</small></div></div>

    <div class="time">6:30pm</div>
    <div class="slot"><div class="class vinyasa">POWER<br>VINYASA<small>60 MINUTES</small></div></div>
    <div class="slot"></div>
    <div class="slot"><div class="class hot">HOT<small>90 MINUTES</small></div></div>
    <div class="slot"><div class="charity">
      <svg width="40" height="38" viewBox="0 0 40 38" role="img" aria-label="Charity class"><polygon points="20,1 24.7,14 39,14 27.5,22.5 31.8,37 20,28.3 8.2,37 12.5,22.5 1,14 15.3,14" fill="var(--charity)"/></svg>
    </div></div>
    <div class="slot"><div class="class funky">FUNKY<br>FLOW<small>75 MINUTES</small></div></div>
    <div class="slot"></div>
    <div class="slot"><div class="class yin">YIN<small>60 MINUTES</small></div></div>

    <div class="time">7:45pm</div>
    <div class="slot"><div class="class essentials compact">POWER<br>ESSENTIALS<small>60 MINUTES</small></div></div>
    <div class="slot"></div>
    <div class="slot"><div class="class vinyasa">POWER<br>VINYASA<small>60 MINUTES</small></div></div>
    <div class="slot"></div><div class="slot"></div><div class="slot"></div><div class="slot"></div>
  </div>

  <aside class="legend">
    <div class="legend-item">
      <span class="legend-tag funky">FUNKY<br>FLOW</span>
      <p class="legend-text">Finish off the week and head into the weekend with a joyful flowing class to a playlist of funky beats.</p>
    </div>
    <div class="legend-item">
      <span class="legend-star"><svg width="26" height="25" viewBox="0 0 40 38" aria-hidden="true"><polygon points="20,1 24.7,14 39,14 27.5,22.5 31.8,37 20,28.3 8.2,37 12.5,22.5 1,14 15.3,14" fill="var(--charity)"/></svg></span>
      <p class="legend-text">Charity class by donation, suggested $10. Please place cash only in the charity donation box. Frequent guest teachers.</p>
    </div>
    <div class="legend-item">
      <span class="legend-tag hot">HOT</span>
      <p class="legend-text">Dynamic sequence of Strength and Breathing exercises. Suitable for beginners. Heat 37 = degrees.</p>
    </div>
    <div class="legend-item">
      <span class="legend-tag essentials" style="font-size:5px;line-height:6px">POWER<br>ESSENTIALS</span>
      <p class="legend-text">Flowing Practice with space and time to Align and understand the poses deeply, building muscular strength and endurance. Ideal for beginners.</p>
    </div>
    <div class="legend-item">
      <span class="legend-tag vinyasa">POWER<br>VINYASA</span>
      <p class="legend-text">Strong, Dynamic, Flowing practice ideal for building physical power, flexibility and mental resilience. Heat = 30 degrees</p>
    </div>
    <div class="legend-item">
      <span class="legend-tag yin">YIN</span>
      <p class="legend-text">Long, Slow, Deep practice with a focus on supporting the body to release our deep internal structures of connective tissue.</p>
    </div>
    <div class="legend-web">www.stillwaterflow.com.au</div>
  </aside>
</section>

</body>
</html>
```